Business Card for Quillmark Ledger - A cannabis publication for executives.

I'd like some business cards for Quillmark Ledger. The logo is done (great job!) and I need a card design I will use with PRINTLY. I made it a short project to allow time for printing before an event. These will be standard sized cards (final artwork size 3.66" x 2.16" at 300dpi) with a final card size of 3.5" x 2.0". (See PRINTLY.com if you need more info.) I might try rounded corners but am not sure yet. I think the design will work okay with rounded.

Quillmark Ledger will be a bi-weekly publication for the cannabis industry. It is targeted to investors and industry executives, not consumers or pot smokers. So our market is more B2B. However I am open to creativity and making the card something people remark on.

My contact for card:

Dana Merrow
Founder/CEO
dana@quillmarkledger.example

2740 Harlow Avenue
Boston MA 02135
(617)555-0194

Target Market(s)

Executives, Industry people and investors in the Cannabis sector.

Contact Information for Business Card

PRINTLY does do double sided and the second side can be the same or different images. Only one side is required but use of the second side would be a bonus.

Font styles to use
Serif
Sans Serif
Decorative

Colors

Designer to choose colors to be used in the design.

Requirements
Must have
• Logo, contact info
Nice to have
• Style and design to make the card stand out in a crowd.

```html
<!DOCTYPE html>
<html lang="en">
<head>
<meta charset="utf-8">
<title>Quillmark Ledger – Business Card</title>
<link rel="stylesheet" href="https://fonts.googleapis.com/css2?family=Open+Sans:wght@400;600;700&display=swap">
<style>
  :root {
    --stage: #d3d4d8;
    --brand-blue: #1176bc;
    --brand-green: #7ab42c;
    --ink: #3a3a3a;
    --paper: #ffffff;
  }
  html, body {
    margin: 0;
    width: 1200px;
    height: 1200px;
    overflow: hidden;
    background: var(--stage);
    font-family: "Open Sans", sans-serif;
  }
  .stage {
    position: relative;
    width: 1200px;
    height: 1200px;
  }
  .card {
    position: absolute;
    width: 640px;
    height: 366px;
    border-radius: 26px;
    box-shadow: 0 6px 18px rgba(0,0,0,0.18);
    overflow: hidden;
  }
  .card--back {
    left: 90px;
    top: 170px;
    background: var(--brand-blue);
    display: flex;
    align-items: center;
    justify-content: center;
  }
  .card--front {
    left: 470px;
    top: 640px;
    background: var(--paper);
  }
  .wordmark {
    display: flex;
    align-items: center;
    gap: 14px;
    font-weight: 600;
    white-space: nowrap;
  }
  .wordmark__dot {
    width: 22px;
    height: 22px;
    border-radius: 50%;
  }
  .card--back .wordmark { color: var(--paper); font-size: 46px; }
  .card--back .wordmark__dot { background: var(--paper); }
  .card--front .wordmark {
    position: absolute;
    left: 44px;
    top: 56px;
    color: var(--brand-blue);
    font-size: 36px;
  }
  .card--front .wordmark__dot { background: var(--brand-green); width: 18px; height: 18px; }
  .contact {
    position: absolute;
    left: 130px;
    top: 150px;
    color: var(--ink);
    font-size: 15px;
    line-height: 1.4;
  }
  .contact__name {
    margin: 0;
    color: var(--brand-blue);
    font-size: 24px;
    font-weight: 700;
    line-height: 1.1;
  }
  .contact__role {
    margin: 0 0 14px;
    color: var(--brand-green);
    font-size: 17px;
  }
  .contact__address { margin: 0 0 14px; }
  .contact__list { list-style: none; margin: 0; padding: 0; }
  .contact__list li { display: flex; align-items: center; gap: 10px; }
  .contact__list svg { width: 14px; height: 14px; fill: var(--brand-green); flex: none; }
</style>
</head>
<body>
<main class="stage">
  <section class="card card--back" aria-label="Card back">
    <div class="wordmark"><span class="wordmark__dot"></span>Quillmark Ledger</div>
  </section>

  <section class="card card--front" aria-label="Card front">
    <div class="wordmark"><span class="wordmark__dot"></span>Quillmark Ledger</div>
    <div class="contact">
      <p class="contact__name">Dana Merrow</p>
      <p class="contact__role">Founder/CEO</p>
      <p class="contact__address">2740 Harlow Avenue<br>Boston MA 02135</p>
      <ul class="contact__list">
        <li>
          <svg viewBox="0 0 16 16" aria-hidden="true"><path d="M3.5 1l2.5 3-1.5 2c.9 2 2.5 3.6 4.5 4.5l2-1.5 3 2.5-1.5 2.5C7 14 2 9 1 2.5z"/></svg>
          (617)555-0194
        </li>
        <li>
          <svg viewBox="0 0 16 16" aria-hidden="true"><path d="M1 3h14v10H1z M1.5 3.5L8 9l6.5-5.5" stroke="#fff" stroke-width="1.2"/></svg>
          dana@quillmarkledger.example
        </li>
        <li>
          <svg viewBox="0 0 16 16" aria-hidden="true"><circle cx="8" cy="8" r="7"/><path d="M1 8h14M8 1c-3 3-3 11 0 14M8 1c3 3 3 11 0 14" stroke="#fff" stroke-width="1" fill="none"/></svg>
          www.quillmarkledger.example
        </li>
      </ul>
    </div>
  </section>
</main>
</body>
</html>
```